Copperfield Hide Renewal Product Label

We need a design for a label to be used on bottles of leather cleaner and conditioner products that will be used in curated kits. We would like it to incorporate our business logo as well as have an area that we can fill in later with the appropriate product name as needed. We would like to see designs that use shades of brown, but we are open to other colors often seen in leather. I am including the Copperfield Hide business Logo below, however again we would prefer to have the label in various shades of browns, rather than the red and grey, more like the mock-up that I am also attaching.

*** I am attaching examples of the types of bottles that will be used. They vary in size from 8 oz to 16 oz. if you are designing a label for a spray bottle they are from 16-32 oz. ***

```html
<!DOCTYPE html>
<html lang="en">
<head>
<meta charset="utf-8">
<title>Copperfield Hide Renewal – Leather Cleaner &amp; Conditioner Label</title>
<link rel="stylesheet" href="https://fonts.googleapis.com/css2?family=Noto+Serif:ital,wght@0,400;1,400&display=swap">
<style>
  :root {
    --page-bg: #f6f6f6;
    --label-top: #de9b89;
    --label-upper: #a4675a;
    --label-dark: #2a1512;
    --label-lower: #9e6b61;
    --label-bottom: #b07d71;
    --panel-dark: #2e1714;
    --panel-edge: #1c0d0b;
    --stitch: #3b1a16;
    --stitch-light: #c56a5e;
    --accent-red: #8b1f1f;
    --text-light: #ffffff;
    --text-soft: #f6e9e4;
  }
  * { margin: 0; padding: 0; box-sizing: border-box; }
  html, body { width: 1200px; height: 848px; overflow: hidden; }
  body { background: var(--page-bg); position: relative; font-family: "Noto Serif", serif; color: var(--text-light); }

  .label {
    position: absolute; left: 408px; top: 45px; width: 384px; height: 758px;
    background: linear-gradient(180deg, var(--label-top) 0%, var(--label-upper) 28%, var(--label-dark) 52%, var(--label-dark) 62%, var(--label-lower) 84%, var(--label-bottom) 100%);
    overflow: hidden;
  }
  .label::after {
    content: ""; position: absolute; inset: 0;
    background: linear-gradient(110deg, rgba(255,255,255,0.08) 0%, rgba(0,0,0,0) 45%, rgba(0,0,0,0.12) 100%);
    pointer-events: none;
  }
  .stitch-frame { position: absolute; left: 0; top: 0; width: 384px; height: 758px; }

  .brand-plate {
    position: absolute; left: 78px; top: 56px; width: 228px; height: 92px;
    background: var(--panel-dark); border-radius: 0 0 10px 10px;
    display: flex; align-items: center; justify-content: center; gap: 10px;
  }
  .brand-dot { width: 40px; height: 40px; border-radius: 50%; background: var(--text-light); flex: none; }
  .brand-name {
    font-weight: 400; font-size: 15px; line-height: 1.2;
    letter-spacing: 1px; text-transform: uppercase; color: var(--text-light);
  }

  .centered { position: absolute; left: 0; width: 384px; text-align: center; white-space: nowrap; }
  .tagline { top: 168px; font-size: 13px; letter-spacing: 0.3px; color: var(--text-soft); }
  .divider { position: absolute; left: 88px; top: 190px; width: 208px; height: 16px; }

  .title-band {
    position: absolute; left: 26px; top: 211px; width: 332px; height: 111px;
    background: var(--panel-dark); border: 3px solid var(--panel-edge); border-radius: 4px;
    box-shadow: 0 2px 6px rgba(0,0,0,0.4);
    display: flex; align-items: center; justify-content: center;
    overflow: hidden;
  }
  .product-name {
    font-weight: 400; font-size: 68px; line-height: 1; letter-spacing: -1px;
    white-space: nowrap;
  }

  .product-type { top: 330px; font-weight: 400; font-size: 32px; line-height: 38px; }

  .claim-band {
    position: absolute; left: 70px; top: 427px; width: 244px; height: 36px;
    background: linear-gradient(90deg, rgba(139,31,31,0) 0%, var(--accent-red) 25%, var(--accent-red) 75%, rgba(139,31,31,0) 100%);
    display: flex; align-items: center; justify-content: center;
    font-size: 19px; white-space: nowrap;
  }

  .benefits { top: 484px; list-style: none; font-style: italic; font-size: 19.5px; text-transform: uppercase; }
  .benefits li { height: 34px; line-height: 28px; }

  .description { top: 600px; font-size: 12.5px; line-height: 15px; color: var(--text-soft); }
  .volume { top: 654px; font-size: 19px; letter-spacing: 0.5px; }
</style>
</head>
<body>
  <div class="label">
    <svg class="stitch-frame" viewBox="0 0 384 758" aria-hidden="true">
      <rect x="50" y="52" width="284" height="653" rx="6" fill="none" stroke="var(--stitch)" stroke-width="3"/>
      <rect x="55" y="57" width="274" height="643" rx="4" fill="none" stroke="var(--stitch-light)" stroke-width="1" stroke-dasharray="8 6" opacity="0.7"/>
    </svg>

    <div class="brand-plate">
      <span class="brand-dot"></span>
      <span class="brand-name">Copperfield<br>Hide Renewal</span>
    </div>

    <p class="centered tagline">PREMIUM LEATHER PRODUCT</p>
    <svg class="divider" viewBox="0 0 208 16" aria-hidden="true">
      <line x1="0" y1="9" x2="86" y2="9" stroke="#fff" stroke-width="1" stroke-dasharray="3 2"/>
      <line x1="122" y1="9" x2="208" y2="9" stroke="#fff" stroke-width="1" stroke-dasharray="3 2"/>
      <text x="104" y="13" text-anchor="middle" fill="#fff" font-size="11">★<tspan font-size="15">★</tspan>★</text>
    </svg>

    <div class="title-band"><h1 class="product-name">LEATHER</h1></div>

    <h2 class="centered product-type">Cleaner &amp;<br>Conditioner</h2>

    <p class="claim-band">Replaces Lost Oils</p>

    <ul class="centered benefits">
      <li>Lift &amp; Suspends Dirt</li>
      <li>Leaves No Residue</li>
      <li>No Chemical Smell</li>
    </ul>

    <p class="centered description">Lorem ipsum dolor sit amet, consec-<br>tetuer adipiscing elit, sed diam</p>

    <p class="centered volume">8 FL OZ</p>
  </div>
</body>
</html>
```